Lifestyle blog needs a website

I have a blog called Kite and Compass. Logo has been done and I also have the wordpress site with a theme already added to it.

The basics are there but I need design expertise to put everything together, make it look great and ready for me to go and in and start using. Basically what is there at the moment needs to be deleted and start again (not a lot - just me playing around). I am not attached to the theme and am happy to go with whatever ideas you can come up with. At the moment I am looking at 3 lifestyle categories (Fashion, Fitness, Feelings) with a contact page so not an extensive build.

Audience will be women over 40 but please don't make this 'frumpy' - it is aimed at the women who act, look and feel younger than their age and so 'pink & fluffy' and 'old & solid' is not the look I am going for.

My deepest apologies for the delay in responding to designs. I had a family matter which took meant I was unable to spend the quality time required to review. I will therefore be reviewing and deciding over this weekend. Once again, my sincere apologies.

Women over 40

• Feeling of being targeted at old market

```html
<!DOCTYPE html>
<html lang="en">
<head>
<meta charset="utf-8">
<title>Kite and Compass</title>
<link href="https://fonts.googleapis.com/css2?family=Oswald:wght@400;500;600&family=Roboto+Condensed:wght@400;700&family=Open+Sans:wght@400;600&display=swap" rel="stylesheet">
<style>
:root{
  --red:#ee3338;
  --ink:#222222;
  --muted:#8a8a8a;
  --band:#ebebeb;
  --white:#ffffff;
  --foot:#2f2f2f;
}
*{box-sizing:border-box;margin:0;padding:0}
html,body{width:1200px;height:4157px;overflow:hidden}
body{position:relative;background:var(--white);font-family:"Open Sans",sans-serif;color:var(--ink)}
.abs{position:absolute}

/* Hero */
.hero{position:absolute;left:0;top:0;width:1200px;height:615px;background:linear-gradient(180deg,#f1f1f1,#e4e4e4);overflow:hidden}
.hero-shape{position:absolute;left:0;top:0}
.hero-photo{position:absolute;left:790px;top:0;width:410px;height:615px;background:linear-gradient(160deg,#e9e9e9 0%,#c9c6c2 40%,#5a6f8e 80%,#3e4e66 100%)}
.brand{position:absolute;left:130px;top:52px;display:flex;align-items:center;gap:14px}
.brand-mark{width:22px;height:22px;background:var(--red)}
.brand-name{font-family:"Oswald",sans-serif;font-weight:500;font-size:40px;color:var(--ink);letter-spacing:.5px}
.search{position:absolute;left:1044px;top:32px}
.hero-title{position:absolute;left:513px;top:148px;font-family:"Oswald",sans-serif;font-size:50px;line-height:60px;color:var(--ink);text-transform:uppercase}
.btn{display:inline-block;background:var(--white);font-family:"Oswald",sans-serif;font-size:15px;color:#444;text-transform:uppercase;padding:10px 18px;box-shadow:0 1px 2px rgba(0,0,0,.1)}
.hero .btn{position:absolute;left:513px;top:343px}
.hero-next{position:absolute;left:1148px;top:262px;width:52px;height:86px;background:#555}
.main-nav{position:absolute;left:130px;top:358px;list-style:none}
.main-nav li{font-family:"Oswald",sans-serif;font-size:21px;color:var(--white);text-transform:uppercase;height:48px;display:flex;align-items:center;gap:10px}
.main-nav li:first-child{text-decoration:underline}

/* Sections */
.band{position:absolute;left:0;width:1200px;background:var(--band)}
.photo{position:absolute}
.section-bar{position:absolute;height:78px;background:var(--red);color:var(--white);font-family:"Oswald",sans-serif;font-weight:500;font-size:46px;text-transform:uppercase;display:flex;align-items:center;justify-content:center}
.articles{position:absolute;width:445px;list-style:none}
.article{display:flex;gap:15px;height:155px}
.thumb{width:160px;height:111px;flex:none}
.article h3{font-family:"Roboto Condensed",sans-serif;font-weight:700;font-size:19px;line-height:23px;color:var(--ink)}
.article time{display:block;font-size:11px;color:#555;margin:8px 0 6px}
.article p{font-size:11px;line-height:15px;color:var(--muted)}
.videos-title{position:absolute;font-family:"Oswald",sans-serif;font-weight:500;font-size:29px;color:var(--red);text-transform:uppercase}
.video{position:absolute;width:222px;height:225px;display:flex;flex-direction:column;align-items:center;justify-content:center;color:var(--white);text-align:center}
.video svg{margin-bottom:14px}
.video span{font-family:"Roboto Condensed",sans-serif;font-weight:700;font-size:19px;line-height:23px;padding:0 16px;text-shadow:0 1px 3px rgba(0,0,0,.6)}
.view-all{position:absolute;background:var(--white);font-family:"Oswald",sans-serif;font-size:15px;color:#444;padding:9px 14px;text-transform:uppercase}

/* Newsletter */
.newsletter h2{position:absolute;left:0;top:3830px;width:1200px;text-align:center;font-family:"Oswald",sans-serif;font-weight:500;font-size:46px;color:var(--red);text-transform:uppercase}
.newsletter p{position:absolute;left:0;top:3898px;width:1200px;text-align:center;font-family:"Roboto Condensed",sans-serif;font-weight:700;font-size:19px;color:var(--ink)}
.field{position:absolute;top:3935px;height:44px;border:1px solid #d4d4d4;background:var(--white);font-family:"Roboto Condensed",sans-serif;font-size:15px;color:#555;padding:12px 12px}
.subscribe{position:absolute;left:801px;top:3935px;width:111px;height:44px;background:var(--red);color:var(--white);font-family:"Oswald",sans-serif;font-size:15px;display:flex;align-items:center;justify-content:center;text-transform:uppercase}

/* Footer */
.site-footer{position:absolute;left:0;top:4060px;width:1200px;height:97px;background:var(--foot);color:#bbb;font-size:12px}
.foot-nav{position:absolute;left:133px;top:26px;display:flex;gap:10px}
.foot-copy{position:absolute;left:133px;top:52px}
.social{position:absolute;left:866px;top:33px;display:flex;gap:20px}
.social i{display:block;width:14px;height:14px;border-radius:50%;background:#9a9a9a}
</style>
</head>
<body>

<header class="hero">
  <div class="hero-photo" role="img" aria-label="Young man in a grey t-shirt and jeans sitting against a white wall"></div>
  <svg class="hero-shape" width="1200" height="615" viewBox="0 0 1200 615">
    <polygon points="0,0 430,0 780,0 430,615 0,615" fill="#f7f7f7"/>
    <polygon points="0,150 560,615 0,615" fill="#ee3338"/>
    <polygon points="0,150 130,250 0,320" fill="#e02c31"/>
  </svg>
  <div class="brand"><span class="brand-mark"></span><span class="brand-name">Kite and Compass</span></div>
  <svg class="search" width="20" height="20" viewBox="0 0 20 20"><circle cx="8" cy="8" r="6" fill="none" stroke="#222" stroke-width="2.4"/><line x1="12.5" y1="12.5" x2="18" y2="18" stroke="#222" stroke-width="2.6"/></svg>
  <h1 class="hero-title">Aenean<br>Faucibus<br>Lacus</h1>
  <span class="btn">View more</span>
  <div class="hero-next"><svg width="52" height="86" viewBox="0 0 52 86"><polyline points="22,31 34,43 22,55" fill="none" stroke="#fff" stroke-width="3"/></svg></div>
  <ul class="main-nav">
    <li>› Fashion</li><li>› Fitness</li><li>› Feelings</li><li>› About</li><li>› Contact</li>
  </ul>
</header>

<!-- Fashion -->
<section class="band" style="top:615px;height:1000px"></section>
<div class="photo" style="left:0;top:615px;width:596px;height:577px;background:linear-gradient(135deg,#e7e4e0,#c9b38f 45%,#9e8a6c 75%,#d6d1c9)" role="img" aria-label="Three friends riding a bicycle, skateboard and rollerblades down a street"></div>
<div class="section-bar" style="left:568px;top:657px;width:632px">Fashion</div>
<ul class="articles" style="left:626px;top:770px">
  <li class="article"><div class="thumb" style="background:linear-gradient(135deg,#dfe7ef,#8aa0b8)" role="img" aria-label="Couple in the snow"></div><div><h3>Donec vestibulum odio sem, ac lao reet massa ullamcorper</h3><time>31 jan, 2018</time><p>Donec molestie nisi et tellus hendrerit vehicula. Nunc eu ligula sed quam pulvinar maximus.</p></div></li>
  <li class="article"><div class="thumb" style="background:linear-gradient(135deg,#eceff2,#4d6a8e)" role="img" aria-label="Man sitting on steps"></div><div><h3>Donec sit amet lectus nec tempor laoreet ac nec nunc</h3><time>31 jan, 2018</time><p>Donec molestie nisi et tellus hendrerit vehicula. Nunc eu ligula sed quam pulvinar maximus.</p></div></li>
  <li class="article"><div class="thumb" style="background:linear-gradient(135deg,#f3d27a,#e3a244)" role="img" aria-label="Two women against a yellow wall"></div><div><h3>Nullam accumsan purus tempus viverra</h3><time>31 jan, 2018</time><p>Donec molestie nisi et tellus hendrerit vehicula. Nunc eu ligula sed quam pulvinar maximus.</p></div></li>
  <li class="article"><div class="thumb" style="background:linear-gradient(135deg,#d9d2cb,#3a3535)" role="img" aria-label="Couple in evening wear"></div><div><h3>Praesent elementum nulla sit amet justo pellentesque scelerisque</h3><time>31 jan, 2018</time><p>Donec molestie nisi et tellus hendrerit vehicula. Nunc eu ligula sed quam pulvinar maximus.</p></div></li>
  <li class="article"><div class="thumb" style="background:linear-gradient(135deg,#e6e6e6,#c5333a)" role="img" aria-label="Woman in a red dress"></div><div><h3>Nam lobortis, purus et fringilla tempus, risus eros dignissim diam</h3><time>31 jan, 2018</time><p>Donec molestie nisi et tellus hendrerit vehicula. Nunc eu ligula sed quam pulvinar maximus.</p></div></li>
</ul>
<h2 class="videos-title" style="left:133px;top:1228px">Videos</h2>
<div class="video" style="left:133px;top:1280px;background:linear-gradient(135deg,#5a5450,#2a2624)" role="img" aria-label="Video still of a wristwatch"><svg width="34" height="34" viewBox="0 0 34 34"><circle cx="17" cy="17" r="17" fill="#fff"/><polygon points="13,10 24,17 13,24" fill="#222"/></svg><span>Vestibulum pharetra diam ex</span></div>
<div class="video" style="left:377px;top:1280px;background:linear-gradient(135deg,#9a8a78,#4a3f36)" role="img" aria-label="Video still of a woman outdoors"><svg width="34" height="34" viewBox="0 0 34 34"><circle cx="17" cy="17" r="17" fill="#fff"/><polygon points="13,10 24,17 13,24" fill="#222"/></svg><span>Mauris placerat eros lorem</span></div>
<span class="view-all" style="left:133px;top:1543px">View all ≫</span>
<span class="view-all" style="left:630px;top:1543px">View all ≫</span>

<!-- Fitness -->
<section class="band" style="top:1663px;height:1000px"></section>
<div class="photo" style="left:601px;top:1663px;width:599px;height:576px;background:linear-gradient(135deg,#b9d8e6,#7fb3cb 50%,#2f3338 85%)" role="img" aria-label="Woman training with suspension straps in a gym"></div>
<div class="section-bar" style="left:0;top:1704px;width:632px">Fitness</div>
<ul class="articles" style="left:133px;top:1815px">
  <li class="article"><div class="thumb" style="background:linear-gradient(135deg,#f0ece4,#8ab36a)" role="img" aria-label="Woman with fresh vegetables"></div><div><h3>Vestibulum facilisis dolor at purus tincidunt port</h3><time>31 jan, 2018</time><p>Donec molestie nisi et tellus hendrerit vehicula. Nunc eu ligula sed quam pulvinar maximus.</p></div></li>
  <li class="article"><div class="thumb" style="background:linear-gradient(135deg,#d8d8d8,#4a4a4a)" role="img" aria-label="Trainer with a client"></div><div><h3>Nam fringilla nulla vel nisl condi mentum</h3><time>31 jan, 2018</time><p>Donec molestie nisi et tellus hendrerit vehicula. Nunc eu ligula sed quam pulvinar maximus.</p></div></li>
  <li class="article"><div class="thumb" style="background:linear-gradient(135deg,#3b5c86,#1d2a3b)" role="img" aria-label="Person lifting a kettlebell"></div><div><h3>Phasellus blandit quam a ipsum gravida dapibus</h3><time>31 jan, 2018</time><p>Donec molestie nisi et tellus hendrerit vehicula. Nunc eu ligula sed quam pulvinar maximus.</p></div></li>
  <li class="article"><div class="thumb" style="background:linear-gradient(135deg,#c7b49a,#6d8a5a)" role="img" aria-label="Group running together"></div><div><h3>Cras sed augue tortor. Suspendis se elit ligula</h3><time>31 jan, 2018</time><p>Donec molestie nisi et tellus hendrerit vehicula. Nunc eu ligula sed quam pulvinar maximus.</p></div></li>
  <li class="article"><div class="thumb" style="background:linear-gradient(135deg,#f1f1f1,#a8adb5)" role="img" aria-label="Runner on a snowy road"></div><div><h3>Sed egestas, nisl id cursus ultric ies, turpis orci rhoncus</h3><time>31 jan, 2018</time><p>Donec molestie nisi et tellus hendrerit vehicula. Nunc eu ligula sed quam pulvinar maximus.</p></div></li>
</ul>
<h2 class="videos-title" style="left:601px;top:2276px">Videos</h2>
<div class="video" style="left:601px;top:2328px;background:linear-gradient(135deg,#7b6656,#3a2e26)" role="img" aria-label="Video still of a woman stretching"><svg width="34" height="34" viewBox="0 0 34 34"><circle cx="17" cy="17" r="17" fill="#fff"/><polygon points="13,10 24,17 13,24" fill="#222"/></svg><span>Donec a nisl vel ante tristique</span></div>
<div class="video" style="left:845px;top:2328px;background:linear-gradient(135deg,#8a6d5c,#3d2c24)" role="img" aria-label="Video still of a workout class"><svg width="34" height="34" viewBox="0 0 34 34"><circle cx="17" cy="17" r="17" fill="#fff"/><polygon points="13,10 24,17 13,24" fill="#222"/></svg><span>Praesent accumsan nunc a condimentum</span></div>
<span class="view-all" style="left:133px;top:2587px">View all ≫</span>
<span class="view-all" style="left:601px;top:2587px">View all ≫</span>

<!-- Feelings -->
<section class="band" style="top:2716px;height:997px"></section>
<div class="photo" style="left:0;top:2716px;width:596px;height:573px;background:linear-gradient(135deg,#f3ece2,#d9bfa0 45%,#8a6a52 80%)" role="img" aria-label="Couple embracing in warm sunlight"></div>
<div class="section-bar" style="left:568px;top:2752px;width:632px">Feelings</div>
<ul class="articles" style="left:626px;top:2862px">
  <li class="article"><div class="thumb" style="background:linear-gradient(135deg,#e2e4e6,#6a7480)" role="img" aria-label="Man relaxing on a sofa"></div><div><h3>Fusce porta arcu mi, aliquet dictum nulla interdum</h3><time>31 jan, 2018</time><p>Donec molestie nisi et tellus hendrerit vehicula. Nunc eu ligula sed quam pulvinar maximus.</p></div></li>
  <li class="article"><div class="thumb" style="background:linear-gradient(135deg,#8a8a6a,#3a3a2e)" role="img" aria-label="Stressed person holding their head"></div><div><h3>Donec quis ex semper, consequat ligula at, efficitur</h3><time>31 jan, 2018</time><p>Donec molestie nisi et tellus hendrerit vehicula. Nunc eu ligula sed quam pulvinar maximus.</p></div></li>
  <li class="article"><div class="thumb" style="background:linear-gradient(135deg,#7fa05a,#3b4f6a)" role="img" aria-label="Smiling couple outdoors"></div><div><h3>Phasellus elementum lacinia quam non pellentesque</h3><time>31 jan, 2018</time><p>Donec molestie nisi et tellus hendrerit vehicula. Nunc eu ligula sed quam pulvinar maximus.</p></div></li>
  <li class="article"><div class="thumb" style="background:linear-gradient(135deg,#f2f2f2,#c4b8ae)" role="img" aria-label="Group of women laughing"></div><div><h3>Aliquam malesuada eros sit amet turpis scelerisque maximus</h3><time>31 jan, 2018</time><p>Donec molestie nisi et tellus hendrerit vehicula. Nunc eu ligula sed quam pulvinar maximus.</p></div></li>
  <li class="article"><div class="thumb" style="background:linear-gradient(135deg,#dbeef7,#9cc8dc)" role="img" aria-label="Woman with arms raised against the sky"></div><div><h3>Maecenas lobortis iaculis efficitur. Nulla facilisi</h3><time>31 jan, 2018</time><p>Donec molestie nisi et tellus hendrerit vehicula. Nunc eu ligula sed quam pulvinar maximus.</p></div></li>
</ul>
<h2 class="videos-title" style="left:133px;top:3324px">Videos</h2>
<div class="video" style="left:133px;top:3375px;background:linear-gradient(135deg,#b08a70,#4a3326)" role="img" aria-label="Video still of a couple"><svg width="34" height="34" viewBox="0 0 34 34"><circle cx="17" cy="17" r="17" fill="#fff"/><polygon points="13,10 24,17 13,24" fill="#222"/></svg><span>Mauris pulvinar volutpat ipsum, nec</span></div>
<div class="video" style="left:377px;top:3375px;background:linear-gradient(135deg,#3f4c5c,#1c232c)" role="img" aria-label="Video still of two people talking"><svg width="34" height="34" viewBox="0 0 34 34"><circle cx="17" cy="17" r="17" fill="#fff"/><polygon points="13,10 24,17 13,24" fill="#222"/></svg><span>Phasellus congue dapi bus sapien</span></div>
<span class="view-all" style="left:133px;top:3636px">View all ≫</span>
<span class="view-all" style="left:630px;top:3636px">View all ≫</span>

<!-- Newsletter -->
<section class="newsletter">
  <h2>Newsletter Signup</h2>
  <p>Integer sapien felis, sodales ut lacus non, dignissim pretium</p>
  <div class="field" style="left:288px;width:239px">Name</div>
  <div class="field" style="left:549px;width:235px">Email</div>
  <div class="subscribe">Subscribe</div>
</section>

<footer class="site-footer">
  <nav class="foot-nav"><span>Fashion</span><span>|</span><span>Fitness</span><span>|</span><span>Feelings</span><span>|</span><span>About</span><span>|</span><span>Contact</span></nav>
  <div class="foot-copy">Copyright © 2018 Kite and Compass. All rights reserved.</div>
  <div class="social"><i></i><i></i><i></i><i></i><i></i><i></i></div>
</footer>

</body>
</html>
```